Harborview Sight Fellowship Hall needs an ad/flyer for convention program

Established in 1949, the Harborview Sight Fellowship Hall's mission is to enrich the lives of blind and visually impaired adults by preparing them for a normal, active life in a society that is principally sighted by encouraging independence.

Located in Quillmont Green in San Diego, California, we are a nonprofit that gives blind and visually impaired people in our community an opportunity to socialize and interact. We help members build skills, confidence, and self-esteem through our various social, recreational, and educational activities. We were founded partially by Otter Society members and receive ongoing funding from them.

We need an 8 1/2 by 11 inch color ad in jpg format. We would like it to be editable. This will be the foundation of our rebranding. The ad will be in a meeting program of the California Otters (californiaotters-example.org) with the goal of highlighting some of our programs in order to solicit donations from individual Otter Societies, preferably ongoing ones.

We would like the ad to be generic enough that we can use the ad for other events and as a flyer in the future. We want the ad/flyer to be classic but eye popping with color. We want the design to reflect a professional and lively organization that loves to serve our members. We don’t entirely love our logo, but it’s what we have for now. Our next task will be a new logo design.

We would like to highlight some of our programs for our members include bingo, blind waterskiing and surfing, cooking and ceramic classes, foreign language classes, self defense classes, yoga, and craft classes. Many of the crafts our members make are sold during fundraisers, and they include blankets, scarves, beaded animals, and more. See a sampling of pictures. We provide transportation to and from our Center, free lunch while at the Center, and food to take home. Many of these activities continue during the pandemic via online platforms. We are doing monthly home deliveries of food to our members.

We need donations to keep our programs going, and we have building repairs & maintenance that we need donations in order to complete. See attached document regarding donations. Please reach out if you have questions. Thank you.

Web address: hvsfh-example.org
Street address: The Harborview Sight Fellowship Hall, 4472 Marrow Ln San Diego, CA 92188
Email address: donation@hvsfh-example.org
To make a donation: https://hvsfh-example.org/donate-2/

Target Market(s)

Donors

Industry/Entity Type

NonProfit

Font styles to use
Sans Serif

Requirements
Must have
• Highlight programs and information on how to make a donation.
Nice to have
• Information on how much each dollar donated will go - see attachment
Should not have
• Unprofessional or sloppy details

```html
<!DOCTYPE html>
<html lang="en">
<head>
<meta charset="utf-8">
<title>Harborview Sight Fellowship Hall – Donation Flyer</title>
<link href="https://fonts.googleapis.com/css2?family=Roboto:wght@400;500;700;900&family=Roboto+Condensed:wght@700&display=swap" rel="stylesheet">
<style>
  :root{
    --navy:#0c3d78;
    --navy-deep:#0a3368;
    --yellow:#ffd500;
    --ink:#1b1b1b;
    --paper:#f3f3f3;
    --white:#ffffff;
  }
  *{box-sizing:border-box;margin:0;padding:0}
  html,body{width:990px;height:1200px;overflow:hidden;background:var(--white)}
  body{font-family:"Roboto",Arial,sans-serif;color:var(--ink)}
  .flyer{position:relative;width:990px;height:1200px;overflow:hidden;
    background:linear-gradient(160deg,var(--white) 0%,var(--paper) 55%,#ececec 100%)}
  .backdrop{position:absolute;inset:0;width:990px;height:1200px}

  .tag-heading{position:absolute;left:60px;display:flex;height:62px;font-weight:900;
    font-size:52px;line-height:62px;letter-spacing:-0.5px}
  .tag-heading span{display:block;text-align:center;height:62px}
  .tag-heading .outlined{border:2px solid var(--white);border-right:none;color:var(--yellow);line-height:58px}
  .tag-heading .filled{background:var(--yellow);color:var(--navy-deep)}
  .did-you-know{top:70px}
  .did-you-know .outlined{width:221px}
  .did-you-know .filled{width:209px}
  .pre-covid{top:537px}
  .pre-covid .outlined{width:138px}
  .pre-covid .filled{width:190px}

  .facts{position:absolute;left:60px;top:168px;width:429px;height:330px;list-style:none;color:var(--white);
    font-size:12.6px;line-height:16.4px}
  .facts::before{content:"";position:absolute;left:10px;top:10px;height:260px;width:1.5px;background:var(--yellow)}
  .facts li{position:absolute;left:0;width:429px;padding-left:32px;text-align:justify}
  .facts li:nth-child(1){top:0}
  .facts li:nth-child(2){top:67px}
  .facts li:nth-child(3){top:165px}
  .facts li:nth-child(4){top:214px}
  .facts li:nth-child(5){top:263px}
  .facts .num{position:absolute;left:0;top:-2px;width:22px;height:22px;border-radius:50%;background:var(--yellow);
    color:var(--navy-deep);font-weight:700;font-size:14px;display:flex;align-items:center;justify-content:center}
  .hl{color:var(--yellow);font-weight:700}

  .tier{position:absolute;left:60px;width:470px}
  .tier-bar{height:41px;width:443px;background:var(--yellow);clip-path:polygon(0 0,94% 0,100% 100%,0 100%);
    font-family:"Roboto Condensed","Roboto",sans-serif;font-weight:700;font-size:23px;color:var(--navy-deep);
    padding:0 0 0 24px;line-height:41px}
  .tier ul{list-style:none;margin-top:10px;font-size:13.2px;font-weight:500}
  .tier li{position:relative;padding-left:25px;height:23px;line-height:18px}
  .check{position:absolute;left:0;top:1px;width:16px;height:16px;border:1.5px solid var(--navy);border-radius:50%}
  .check::after{content:"";position:absolute;left:4.5px;top:2px;width:4px;height:7px;border:solid var(--navy);
    border-width:0 1.5px 1.5px 0;transform:rotate(45deg)}
  .tier-10{top:634px}.tier-20{top:771px}.tier-50{top:884px}.tier-100{top:997px}

  .photo{position:absolute;border-radius:50%}
  .photo-penguin{left:527px;top:49px;width:450px;height:450px;background:radial-gradient(circle at 55% 40%,#6d6d6d 0%,#3f3f3f 40%,#cfcfcf 80%,#e9e9e9 100%)}
  .photo-blankets{left:497px;top:403px;width:290px;height:280px;background:linear-gradient(180deg,#4d9fd0 0%,#e7a9c4 30%,#e8e8ee 50%,#8e6fc1 70%,#65c4c6 100%)}
  .photo-angel{left:751px;top:476px;width:200px;height:196px;background:radial-gradient(circle at 45% 65%,#2a5fc8 0%,#7f8ea8 45%,#d9d9d9 100%)}

  .contact{position:absolute;left:581px;top:640px;width:350px;height:249px;background:var(--yellow);border-radius:0 0 16px 16px;
    padding:58px 0 0 47px;font-size:14.6px;line-height:1.2}
  .contact h3{font-size:16px;font-weight:700;margin-bottom:8px}
  .contact .row{position:relative;margin-bottom:6px}
  .contact .row svg{position:absolute;left:-21px;top:1px}
  .donate-head{position:absolute;left:602px;top:845px;width:308px;height:33px;background:var(--navy-deep);border-radius:5px 5px 0 0;
    color:var(--yellow);font-family:"Roboto Condensed","Roboto",sans-serif;font-weight:700;font-size:19px;text-align:center;line-height:33px}
  .donate-url{position:absolute;left:602px;top:878px;width:308px;height:32px;background:var(--white);border-radius:0 0 5px 5px;
    box-shadow:0 6px 8px -6px rgba(0,0,0,.35);font-size:15px;font-weight:500;text-align:center;line-height:31px}

  .org-mark{position:absolute;left:622px;top:965px;width:280px;display:flex;align-items:center;justify-content:center;gap:12px;
    font-size:40px;font-weight:900;color:var(--ink)}
  .org-mark .square{width:26px;height:26px;background:var(--ink)}

  .footer-band{position:absolute;left:0;top:1090px;width:990px;height:110px;background:var(--navy-deep);border-top:3px solid var(--yellow);
    color:var(--yellow);font-weight:700;font-size:18.5px;text-align:center;padding-top:23px;line-height:1.7}
</style>
</head>
<body>
<main class="flyer">
  <svg class="backdrop" viewBox="0 0 990 1200" aria-hidden="true">
    <path d="M0 0H655C600 150 565 390 505 560C445 640 300 650 0 568Z" fill="#0c3d78"/>
    <path d="M0 592C170 640 330 660 500 620" fill="none" stroke="#ffd500" stroke-width="1.5"/>
    <path d="M628 0C660 40 690 60 700 60" fill="none" stroke="#ffd500" stroke-width="1.5"/>
    <path d="M700 60C760 30 900 20 980 30" fill="none" stroke="#ffd500" stroke-width="1.5"/>
    <circle cx="752" cy="274" r="238" fill="none" stroke="#ffd500" stroke-width="1.5"/>
    <circle cx="642" cy="543" r="153" fill="none" stroke="#ffd500" stroke-width="1.5"/>
    <circle cx="851" cy="574" r="108" fill="none" stroke="#ffd500" stroke-width="1.5"/>
  </svg>

  <h1 class="tag-heading did-you-know"><span class="outlined">Did You</span><span class="filled">Know?</span></h1>

  <ol class="facts">
    <li><span class="num">1</span>During the pandemic we offer Bingo, Trivia and other virtual games every week, where blind and low vision participants can win HSF bucks. <span class="hl">You can sponsor one day of games for $35.</span></li>
    <li><span class="num">2</span>You can provide 75 gift bags for our ‘We are in This Together’ home delivery program. Many of our blind and low vision people are isolated and stuck at home. These gift packages are welcomed with enthusiasm and gratefulness. Your rewards are huge smiles and happy faces.</li>
    <li><span class="num">3</span>Our building is over 20 years old and requires ongoing maintenance and repairs</li>
    <li class="hl"><span class="num">4</span>Fencing (cage) required to protect outside air conditioning units from vandalism. Cost: $2,500</li>
    <li><span class="num">5</span>Wanted: Sponsors for weekly virtual bingo and trivia games: Blind and Low vision participants receive one HSF buck per win. HSF bucks are turned into gift cards and Bayline transportation passes. <span class="hl">Sponsor one week for $40. Sponsor 1 month for $160</span></li>
  </ol>

  <h2 class="tag-heading pre-covid"><span class="outlined">Pre-</span><span class="filled">Covid</span></h2>

  <section class="tier tier-10">
    <div class="tier-bar">$10 per month or $120 will buy:</div>
    <ul>
      <li><span class="check"></span>60 meals for our lunch program – we serve 130 meals each week</li>
      <li><span class="check"></span>13 round trip Bayline transportation tickets</li>
      <li><span class="check"></span>Enough beads to make 35 Marigold angels in our craft class</li>
    </ul>
  </section>
  <section class="tier tier-20">
    <div class="tier-bar">$20 per month or $240 will buy:</div>
    <ul>
      <li><span class="check"></span>26 round trip Bayline transportation tickets</li>
      <li><span class="check"></span>One month of large print and Braille translation newsletter printing</li>
    </ul>
  </section>
  <section class="tier tier-50">
    <div class="tier-bar">$50 per month or $600 will buy:</div>
    <ul>
      <li><span class="check"></span>300 lunches</li>
      <li><span class="check"></span>Thanksgiving dinner with all the fixings for 80 to 100 guests</li>
    </ul>
  </section>
  <section class="tier tier-100">
    <div class="tier-bar">$100 per month or $1200 will buy:</div>
    <ul>
      <li><span class="check"></span>Approximately 10 Bingo parties including food and prizes</li>
    </ul>
  </section>

  <div class="photo photo-penguin" role="img" aria-label="Photo of a beaded penguin in a Santa hat resting on a white knitted blanket"></div>

  <div class="contact">
    <h3>Street address:</h3>
    <div class="row">
      <svg width="12" height="16" viewBox="0 0 12 16" aria-hidden="true"><circle cx="6" cy="5" r="3.5" fill="none" stroke="#1b1b1b" stroke-width="1.3"/><path d="M6 8.5V15M3 15H9" stroke="#1b1b1b" stroke-width="1.3"/></svg>
      The Harborview Sight Fellowship Hall,<br>4472 Marrow Ln San Diego, CA 92188
    </div>
    <div class="row">
      <svg width="14" height="12" viewBox="0 0 14 12" aria-hidden="true"><rect x="1" y="1.5" width="12" height="9" fill="none" stroke="#1b1b1b" stroke-width="1.2"/><path d="M1 1.5L7 7L13 1.5M1 10.5L5.5 6M13 10.5L8.5 6" fill="none" stroke="#1b1b1b" stroke-width="1.2"/></svg>
      donation@hvsfh-example.org
    </div>
    <div class="row">
      <svg width="14" height="14" viewBox="0 0 14 14" aria-hidden="true"><circle cx="7" cy="7" r="6" fill="none" stroke="#1b1b1b" stroke-width="1.2"/><ellipse cx="7" cy="7" rx="2.6" ry="6" fill="none" stroke="#1b1b1b" stroke-width="1.2"/><path d="M1 7H13M2 4H12M2 10H12" stroke="#1b1b1b" stroke-width="1"/></svg>
      www.hvsfh-example.org
    </div>
  </div>

  <div class="photo photo-blankets" role="img" aria-label="Photo of a stack of colorful hand-knitted blankets"></div>
  <div class="photo photo-angel" role="img" aria-label="Photo of a blue beaded angel ornament"></div>

  <div class="donate-head">TO MAKE A DONATION:</div>
  <div class="donate-url">https://hvsfh-example.org/donate-2/</div>

  <div class="org-mark"><span class="square"></span>HSF Hall</div>

  <footer class="footer-band">
    $1,083 per month or $13,000 per year will fund our entire lunch program for the year.<br>
    Every dollar donated goes to support HSF participants and programs.
  </footer>
</main>
</body>
</html>
```